Brightwell Auto Care 4x9 Rack Card

Design a 4" wide by 9" tall rack card printed front and back using the copy, logo and images uploaded below. I am also uploading a current flyer so you can see the typestyles we use. I will get the exact name of the font for you ASAP. Also will be uploading some before and after pictures for the back of the rack card

Target Market(s)

Affluent consumers who need their car cleaned and detailed in a meticulous fashion

Requirements
Must have
• Under the logo, put the words...... Premium Steam Detailing & Ceramic Coating.........also put ther following wording on the front side: Get Steamed! We use steam to clean your vehicle helping save millions of gallons of water and protecting our rivers, streams and lakes from runoff.
Nice to have
• a screened back background of hexagons might be nice

```html
<!DOCTYPE html>
<html lang="en">
<head>
<meta charset="utf-8">
<title>Brightwell Auto Care Rack Card</title>
<link href="https://fonts.googleapis.com/css2?family=Michroma&family=Montserrat:wght@400;600;700;800&family=Oswald:wght@500&display=swap" rel="stylesheet">
<style>
:root{
  --green:#6aab45;
  --blue:#3f7ec6;
  --black:#0d0d0d;
  --white:#ffffff;
  --ink:#2b2b2b;
  --stage:#f1f1f1;
  --photo-a:#c9b48e;
  --photo-b:#2d4f7c;
  --photo-c:#5c6670;
}
*{margin:0;padding:0;box-sizing:border-box}
html,body{width:800px;height:1200px;overflow:hidden;background:var(--stage)}
body{position:relative;font-family:"Montserrat",sans-serif;color:var(--ink)}
.card{position:absolute;top:195px;width:360px;height:810px;background:var(--white);overflow:hidden;box-shadow:0 4px 14px rgba(0,0,0,.18)}
.card--front{left:27px}
.card--back{left:413px}
.abs{position:absolute}
.center{left:0;right:0;text-align:center}

/* front */
.front-top{left:0;top:0;width:360px;height:212px;background:var(--black)}
.brand{left:0;right:0;top:38px;display:flex;align-items:center;justify-content:center;gap:12px}
.brand__dot{width:46px;height:46px;border-radius:50%;background:var(--green);flex:none}
.brand__name{font-family:"Michroma",sans-serif;color:var(--green);font-size:19px;line-height:1.35;letter-spacing:1px}
.tag-premium{top:120px;font-family:"Michroma",sans-serif;font-size:34px;color:var(--green);font-weight:700;letter-spacing:1px}
.tag-steam{top:162px;font-family:"Michroma",sans-serif;font-size:19px;color:var(--white)}
.tag-ceramic{top:187px;font-family:"Michroma",sans-serif;font-size:19px;color:var(--blue)}
.front-photo{left:0;top:212px}
.get-steamed{top:480px;font-weight:800;font-size:22px;color:var(--green)}
.mission{top:512px;left:30px;right:30px;text-align:center;font-size:10px;line-height:1.25}
.addr{display:flex;align-items:center;height:24px}
.addr__bar{background:var(--green);color:var(--black);font-size:9px;font-weight:600;line-height:1.05;padding:2px 8px 2px 16px;height:22px;display:flex;flex-direction:column;justify-content:center;clip-path:polygon(0 0,100% 0,94% 100%,0 100%);flex:1}
.addr__pin{width:26px;height:26px;border-radius:50%;background:var(--white);border:2px solid var(--blue);display:flex;align-items:center;justify-content:center;margin-right:-12px;position:relative;z-index:1;flex:none}
.call-1{top:626px;font-size:13px;color:var(--blue);font-weight:600}
.call-2{top:641px;font-size:13px;color:var(--green);font-weight:700}
.phones{display:flex;gap:4px}
.phone{position:relative;width:98px;height:42px;border:2px solid var(--blue);border-radius:6px;text-align:center;padding-top:13px}
.phone__icon{position:absolute;top:-13px;left:50%;margin-left:-12px;width:24px;height:24px;border-radius:50%;background:var(--green);border:2px solid var(--white);display:flex;align-items:center;justify-content:center}
.phone__town{font-size:8px;font-weight:600;color:var(--black)}
.phone__num{font-size:11px;font-weight:600;color:var(--green)}
.slogan-band{left:0;bottom:0}
.slogan{bottom:22px;font-family:"Michroma",sans-serif;font-size:10.5px;color:var(--white);font-weight:700}
.slogan .g{color:var(--green)}

/* back */
.back-photo{left:0;top:0}
.label{height:24px;padding:0 14px;border-radius:12px 12px 0 12px;font-weight:700;font-size:13px;color:var(--white);display:flex;align-items:center;letter-spacing:.5px}
.label--before{background:var(--blue)}
.label--after{background:var(--green)}
.brand--small{left:33px;right:auto;top:290px;gap:8px;justify-content:flex-start}
.brand--small .brand__dot{width:30px;height:30px}
.brand--small .brand__name{font-size:11px;line-height:1.3;letter-spacing:.5px}
.svc{font-weight:700;font-size:12.5px;color:var(--blue);line-height:1.2;border-left:1.5px solid var(--green);padding-left:5px}
.svc small{display:block;font-weight:400;color:var(--ink);font-size:10px}
.price{text-align:center;color:var(--green);font-family:"Oswald",sans-serif;font-size:27px;line-height:1}
.price small{display:block;font-family:"Montserrat",sans-serif;font-size:9px;color:var(--ink);line-height:1.2}
.ceramic{top:563px;font-family:"Michroma",sans-serif;font-size:18px;color:var(--blue);font-weight:700}
.rule{top:594px;left:145px;width:70px;height:2px;background:var(--blue)}
.quote-1{top:606px;font-size:13px;color:var(--blue);font-weight:700}
.quote-2{top:620px;font-size:13px;color:var(--blue);font-weight:700}
</style>
</head>
<body>

<!-- FRONT -->
<section class="card card--front">
  <div class="abs front-top"></div>
  <div class="abs brand">
    <span class="brand__dot"></span>
    <span class="brand__name">BRIGHTWELL<br>AUTO CARE</span>
  </div>
  <div class="abs center tag-premium">PREMIUM</div>
  <div class="abs center tag-steam">STEAM DETAILING</div>
  <div class="abs center tag-ceramic">&amp; CERAMIC COATING</div>

  <svg class="abs front-photo" width="360" height="258" viewBox="0 0 360 258" role="img" aria-label="Hexagon collage of a technician steam cleaning the front grille of a luxury car">
    <defs>
      <linearGradient id="photoFront" x1="0" y1="0" x2="1" y2="1">
        <stop offset="0" stop-color="var(--photo-a)"/>
        <stop offset=".55" stop-color="var(--photo-c)"/>
        <stop offset="1" stop-color="var(--photo-b)"/>
      </linearGradient>
    </defs>
    <rect width="360" height="258" fill="var(--black)"/>
    <polygon points="0,10 45,10 75,80 0,150" fill="var(--blue)"/>
    <polygon points="360,130 360,258 300,258 300,200" fill="var(--green)"/>
    <rect y="248" width="360" height="10" fill="var(--white)"/>
    <g fill="url(#photoFront)" stroke="var(--white)" stroke-width="5">
      <polygon points="94,60 117,20 163,20 186,60 163,100 117,100"/>
      <polygon points="234,60 257,20 303,20 326,60 303,100 257,100"/>
      <polygon points="24,140 47,100 93,100 116,140 93,180 47,180"/>
      <polygon points="164,140 187,100 233,100 256,140 233,180 187,180"/>
      <polygon points="304,140 327,100 373,100 396,140 373,180 327,180"/>
      <polygon points="94,220 117,180 163,180 186,220 163,260 117,260"/>
      <polygon points="234,220 257,180 303,180 326,220 303,260 257,260"/>
    </g>
  </svg>

  <div class="abs center get-steamed">GET STEAMED!</div>
  <p class="abs mission">We use steam to clean your vehicle helping save millions of gallons of water and protecting our rivers, streams and lakes from runoff.</p>

  <div class="abs addr" style="left:31px;top:557px;width:300px">
    <span class="addr__pin"><svg width="12" height="14" viewBox="0 0 12 14"><path d="M6 0a5 5 0 0 0-5 5c0 4 5 9 5 9s5-5 5-9a5 5 0 0 0-5-5zm0 7a2 2 0 1 1 0-4 2 2 0 0 1 0 4z" fill="var(--green)"/></svg></span>
    <span class="addr__bar"><span>412 Larkspur Avenue @ Lakeside Commons</span><span>Harbor Vale</span></span>
  </div>
  <div class="abs addr" style="left:31px;top:588px;width:148px">
    <span class="addr__pin"><svg width="12" height="14" viewBox="0 0 12 14"><path d="M6 0a5 5 0 0 0-5 5c0 4 5 9 5 9s5-5 5-9a5 5 0 0 0-5-5zm0 7a2 2 0 1 1 0-4 2 2 0 0 1 0 4z" fill="var(--green)"/></svg></span>
    <span class="addr__bar"><span>58 Ferncliff Rd</span><span>#104 Cedar Hollow</span></span>
  </div>
  <div class="abs addr" style="left:184px;top:588px;width:148px">
    <span class="addr__pin"><svg width="12" height="14" viewBox="0 0 12 14"><path d="M6 0a5 5 0 0 0-5 5c0 4 5 9 5 9s5-5 5-9a5 5 0 0 0-5-5zm0 7a2 2 0 1 1 0-4 2 2 0 0 1 0 4z" fill="var(--green)"/></svg></span>
    <span class="addr__bar"><span>19 Quarry Lane</span><span>Maple Ridge</span></span>
  </div>

  <div class="abs center call-1">CALL FOR</div>
  <div class="abs center call-2">INFORMATION &amp; SCHEDULING</div>

  <div class="abs phones" style="left:29px;top:680px">
    <div class="phone"><span class="phone__icon"><svg width="12" height="12" viewBox="0 0 24 24"><path d="M6.6 10.8a15 15 0 0 0 6.6 6.6l2.2-2.2a1 1 0 0 1 1-.25 11 11 0 0 0 3.6.6 1 1 0 0 1 1 1V20a1 1 0 0 1-1 1A17 17 0 0 1 3 4a1 1 0 0 1 1-1h3.5a1 1 0 0 1 1 1 11 11 0 0 0 .6 3.6 1 1 0 0 1-.25 1z" fill="var(--white)"/></svg></span><div class="phone__town">Harbor Vale</div><div class="phone__num">(555) 210-4400</div></div>
    <div class="phone"><span class="phone__icon"><svg width="12" height="12" viewBox="0 0 24 24"><path d="M6.6 10.8a15 15 0 0 0 6.6 6.6l2.2-2.2a1 1 0 0 1 1-.25 11 11 0 0 0 3.6.6 1 1 0 0 1 1 1V20a1 1 0 0 1-1 1A17 17 0 0 1 3 4a1 1 0 0 1 1-1h3.5a1 1 0 0 1 1 1 11 11 0 0 0 .6 3.6 1 1 0 0 1-.25 1z" fill="var(--white)"/></svg></span><div class="phone__town">Cedar Hollow</div><div class="phone__num">(555) 318-2290</div></div>
    <div class="phone"><span class="phone__icon"><svg width="12" height="12" viewBox="0 0 24 24"><path d="M6.6 10.8a15 15 0 0 0 6.6 6.6l2.2-2.2a1 1 0 0 1 1-.25 11 11 0 0 0 3.6.6 1 1 0 0 1 1 1V20a1 1 0 0 1-1 1A17 17 0 0 1 3 4a1 1 0 0 1 1-1h3.5a1 1 0 0 1 1 1 11 11 0 0 0 .6 3.6 1 1 0 0 1-.25 1z" fill="var(--white)"/></svg></span><div class="phone__town">Maple Ridge</div><div class="phone__num">(555) 427-6615</div></div>
  </div>

  <svg class="abs slogan-band" width="360" height="76" viewBox="0 0 360 76">
    <polygon points="0,50 22,0 338,0 360,50 360,76 0,76" fill="var(--green)"/>
    <polygon points="8,56 28,8 332,8 352,56 352,76 8,76" fill="var(--black)"/>
    <rect y="68" width="360" height="8" fill="var(--black)"/>
  </svg>
  <div class="abs center slogan">FALL IN <span class="g">LOVE</span> WITH <span class="g">YOUR CAR</span> AGAIN!</div>
</section>

<!-- BACK -->
<section class="card card--back">
  <svg class="abs back-photo" width="360" height="335" viewBox="0 0 360 335" role="img" aria-label="Hexagon collage of before and after photos of a car interior and engine bay">
    <defs>
      <linearGradient id="photoBack" x1="0" y1="0" x2="1" y2="1">
        <stop offset="0" stop-color="#8e949a"/>
        <stop offset=".5" stop-color="#3b3f45"/>
        <stop offset="1" stop-color="#1f2226"/>
      </linearGradient>
      <linearGradient id="fadeBack" x1="0" y1="0" x2="0" y2="1">
        <stop offset="0" stop-color="#d9dde1"/>
        <stop offset="1" stop-color="var(--white)"/>
      </linearGradient>
    </defs>
    <rect width="360" height="335" fill="url(#fadeBack)"/>
    <polygon points="0,20 40,20 40,170 0,170" fill="var(--green)"/>
    <polygon points="320,0 360,0 360,60 330,40" fill="var(--green)"/>
    <polygon points="330,100 360,100 360,270 340,230" fill="var(--blue)"/>
    <g fill="url(#photoBack)" stroke="var(--white)" stroke-width="5">
      <polygon points="22,70 61,2 139,2 178,70 139,138 61,138"/>
      <polygon points="180,95 219,27 297,27 336,95 297,163 219,163"/>
      <polygon points="27,205 66,137 144,137 183,205 144,273 66,273"/>
      <polygon points="180,255 219,187 297,187 336,255 297,323 219,323"/>
    </g>
  </svg>
  <div class="abs label label--before" style="left:58px;top:70px">BEFORE</div>
  <div class="abs label label--after" style="left:198px;top:148px">AFTER</div>
  <div class="abs label label--before" style="left:58px;top:230px">BEFORE</div>
  <div class="abs label label--after" style="left:198px;top:311px">AFTER</div>

  <div class="abs brand brand--small">
    <span class="brand__dot"></span>
    <span class="brand__name">BRIGHTWELL<br>AUTO CARE</span>
  </div>

  <div class="abs svc" style="left:33px;top:375px">Premium<br>Steam<br>Washes</div>
  <div class="abs price" style="left:125px;top:370px;width:62px"><small>Starting at</small>$100<small>and up</small></div>
  <div class="abs svc" style="left:194px;top:375px">Full<br>Steam<br>Detailing</div>
  <div class="abs price" style="left:265px;top:370px;width:62px"><small>Starting at</small>$275<small>and up</small></div>

  <div class="abs svc" style="left:33px;top:437px">Headlight<br>Restoration</div>
  <div class="abs price" style="left:125px;top:443px;width:62px">$110</div>
  <div class="abs svc" style="left:194px;top:437px">Engine<br>Steam<br>Cleaning</div>
  <div class="abs price" style="left:265px;top:443px;width:52px">$75</div>

  <div class="abs svc" style="left:80px;top:497px">Paint<br>Correction<small>(multi-stage polishing)</small></div>
  <div class="abs price" style="left:210px;top:487px;width:62px"><small>Starting at</small>$650<small>and up</small></div>

  <div class="abs center ceramic">CERAMIC COATING</div>
  <div class="abs rule"></div>
  <div class="abs center quote-1">CALL OR VISIT</div>
  <div class="abs center quote-2">US FOR A QUOTE</div>

  <div class="abs phones" style="left:27px;top:666px">
    <div class="phone"><span class="phone__icon"><svg width="12" height="12" viewBox="0 0 24 24"><path d="M6.6 10.8a15 15 0 0 0 6.6 6.6l2.2-2.2a1 1 0 0 1 1-.25 11 11 0 0 0 3.6.6 1 1 0 0 1 1 1V20a1 1 0 0 1-1 1A17 17 0 0 1 3 4a1 1 0 0 1 1-1h3.5a1 1 0 0 1 1 1 11 11 0 0 0 .6 3.6 1 1 0 0 1-.25 1z" fill="var(--white)"/></svg></span><div class="phone__town">Harbor Vale</div><div class="phone__num">(555) 210-4400</div></div>
    <div class="phone"><span class="phone__icon"><svg width="12" height="12" viewBox="0 0 24 24"><path d="M6.6 10.8a15 15 0 0 0 6.6 6.6l2.2-2.2a1 1 0 0 1 1-.25 11 11 0 0 0 3.6.6 1 1 0 0 1 1 1V20a1 1 0 0 1-1 1A17 17 0 0 1 3 4a1 1 0 0 1 1-1h3.5a1 1 0 0 1 1 1 11 11 0 0 0 .6 3.6 1 1 0 0 1-.25 1z" fill="var(--white)"/></svg></span><div class="phone__town">Cedar Hollow</div><div class="phone__num">(555) 318-2290</div></div>
    <div class="phone"><span class="phone__icon"><svg width="12" height="12" viewBox="0 0 24 24"><path d="M6.6 10.8a15 15 0 0 0 6.6 6.6l2.2-2.2a1 1 0 0 1 1-.25 11 11 0 0 0 3.6.6 1 1 0 0 1 1 1V20a1 1 0 0 1-1 1A17 17 0 0 1 3 4a1 1 0 0 1 1-1h3.5a1 1 0 0 1 1 1 11 11 0 0 0 .6 3.6 1 1 0 0 1-.25 1z" fill="var(--white)"/></svg></span><div class="phone__town">Maple Ridge</div><div class="phone__num">(555) 427-6615</div></div>
  </div>

  <svg class="abs slogan-band" width="360" height="76" viewBox="0 0 360 76">
    <polygon points="0,50 22,0 338,0 360,50 360,76 0,76" fill="var(--green)"/>
    <polygon points="8,56 28,8 332,8 352,56 352,76 8,76" fill="var(--black)"/>
    <rect y="68" width="360" height="8" fill="var(--black)"/>
  </svg>
  <div class="abs center slogan">FALL IN <span class="g">LOVE</span> WITH <span class="g">YOUR CAR</span> AGAIN!</div>
</section>

</body>
</html>
```